Webdesign für Lindenhof
Zielgruppe
Lindenhof Brauckmann:
Zielgruppe sind alle, die gern Fisch essen. Es gibt einen Hofladen, einen Partyservice, eine Gaststätte und eine kleine Pension. Wichtig wäre darzustellen, dass es in der Gaststätte außer Fisch auch Fleisch gibt.
Einen Einblick geben Ihnen die Webseite und der beiliegende Flyer.
Aufgabenstellung
Die Öffnungszeiten von Gaststätte und Hofladen sollten prominent dargestellt werden. Neben den eigenen Bildern sollen auch stock-Fotos genutzt werden.

```html
<!DOCTYPE html>
<html lang="de">
<head>
<meta charset="utf-8">
<title>Lindenhof Brauckmann</title>
<link href="https://fonts.googleapis.com/css2?family=Kaushan+Script&family=Great+Vibes&family=Raleway:wght@400;600;700;800&display=swap" rel="stylesheet">
<style>
:root{
  --gold:#c39a5b;
  --ink:#1b1b1b;
  --dark:#161616;
  --muted:#9a9a9a;
  --line:#e6e6e6;
  --white:#ffffff;
}
*{margin:0;padding:0;box-sizing:border-box}
html,body{width:1200px;height:3816px;overflow:hidden;background:var(--white)}
body{position:relative;font-family:"Raleway",sans-serif;color:var(--ink)}
.abs{position:absolute}
.center{text-align:center}
.script-gold{font-family:"Great Vibes",cursive;color:var(--gold)}
.script-head{font-family:"Kaushan Script",cursive;color:var(--ink)}
.body-text{font-size:11px;line-height:16px;color:var(--muted)}
.price{font-family:"Kaushan Script",cursive;color:var(--gold);font-size:16px}
.chevrons{color:var(--gold);font-size:15px;letter-spacing:6px;font-weight:700}

/* Hero */
.hero{left:0;top:0;width:1200px;height:486px;background:radial-gradient(ellipse at 20% 20%,#4a4642 0%,#2b2826 45%,#1c1a19 100%)}
.hero-shade{left:0;top:0;width:1200px;height:486px;background:rgba(0,0,0,.25)}
.nav{right:212px;top:27px;display:flex;gap:24px}
.nav a{color:var(--white);font-size:9px;font-weight:800;text-decoration:none;letter-spacing:.3px}
.nav-rule{left:0;top:67px;width:1200px;height:1px;background:rgba(255,255,255,.12)}
.hero-kicker{left:0;width:1200px;top:126px;font-size:32px;color:var(--white)}
.hero-title{left:0;width:1200px;top:158px;font-family:"Kaushan Script",cursive;font-size:58px;color:var(--white)}
.hero-text{left:300px;width:600px;top:235px;color:var(--white);font-size:12px;font-weight:700;line-height:19px}
.dots{display:flex;gap:8px}
.dot{width:9px;height:9px;border-radius:50%;border:1.5px solid var(--white)}
.dot.on{background:var(--white)}
.dots.dark .dot{border-color:#222}
.dots.dark .dot.on{background:#222}

/* Tabs */
.tabs{left:0;width:1200px;top:562px;display:flex;justify-content:center;gap:30px;font-family:"Kaushan Script",cursive;font-size:15px}
.tabs span{padding-bottom:6px}
.tabs .active{color:var(--gold);border-bottom:2px solid var(--gold)}

.house-card{width:250px;top:615px;text-align:center}
.house-card .photo{width:250px;height:166px}
.house-card .kicker{font-size:24px;margin-top:18px;line-height:28px}
.house-card h3{font-family:"Kaushan Script",cursive;font-weight:400;font-size:19px;margin-top:4px}
.house-card p{margin:10px 12px 0}

/* Sections */
.sec-kicker{left:0;width:1200px;font-size:30px;text-align:center}
.sec-title{left:0;width:1200px;font-size:35px;text-align:center}
.dish{left:300px;width:600px;text-align:center}
.dish h4{font-family:"Kaushan Script",cursive;font-weight:400;font-size:16px;margin-top:6px}
.dish p{margin-top:6px}
.diamond{left:593px}

.spec{width:360px;text-align:center}
.spec .kicker{font-size:30px;line-height:32px}
.spec h3{font-family:"Kaushan Script",cursive;font-weight:400;font-size:32px;margin-top:2px}
.spec .chevrons{margin-top:4px}
.spec p{margin-top:14px}
.spec .price{display:block;margin-top:30px}
.shot{box-shadow:0 0 0 1px rgba(0,0,0,.04)}

.event{top:3010px;width:177px;height:340px;background:var(--white);box-shadow:0 2px 10px rgba(0,0,0,.08)}
.event .photo{height:134px}
.event h4{font-size:13px;font-weight:700;margin:26px 20px 0;line-height:17px}
.event p{font-size:9.5px;line-height:16px;color:var(--muted);margin:18px 20px 0}
.event .date{position:absolute;left:20px;right:20px;bottom:10px;border-top:1px solid #eee;padding-top:12px;font-size:7px;color:#555}

.hours{width:250px;height:249px;top:3404px;background:var(--dark);color:#ddd}
.hours h3{font-family:"Kaushan Script",cursive;font-weight:400;font-size:18px;color:var(--white);text-align:center;margin-top:18px}
.hours .orn{text-align:center;margin-top:8px}
.hours .rule{height:1px;background:#2f2f2f;margin:8px 0 0}
.hours ul{list-style:none;margin:12px 28px 0}
.hours li{display:flex;justify-content:space-between;font-size:8.5px;height:25px;line-height:25px;border-bottom:1px solid #262626}
.bump{top:-14px;left:95px}

.address{left:0;width:1200px;top:3696px;text-align:center;font-size:8.5px;color:#444}
.footer{left:0;top:3752px;width:1200px;height:64px;background:var(--dark)}
.footer-text{top:3779px;font-size:8.5px;color:#ddd}
</style>
</head>
<body>

<header>
  <div class="abs hero" role="img" aria-label="Dunkles Foto eines frischen Fisches mit Zwiebelringen, Chili und Gewürzen auf Holz"></div>
  <div class="abs hero-shade"></div>
  <nav class="abs nav"><a>HOME</a><a>RESTAURANT</a><a>ANGEBOTE</a><a>ÜBER UNS</a><a>KONTAKT</a></nav>
  <div class="abs nav-rule"></div>
  <div class="abs hero-kicker script-gold center" style="color:#fff">Herzlich Willkommen Im</div>
  <h1 class="abs hero-title center" style="font-weight:400">Lindenhof Brauckmann</h1>
  <p class="abs hero-text center">Lorem ipsum dolor sit amet, consetetur sadipscing elitr, sed diam nonumy eirmod tempor invidunt ut labore et dolore magna aliquyam erat, sed diam voluptua. At vero eos et accusam et</p>
  <div class="abs dots" style="left:593px;top:453px"><span class="dot on"></span><span class="dot"></span><span class="dot"></span></div>
</header>

<section class="about">
  <div class="abs tabs"><span class="active">Über Uns</span><span>Historie</span><span>Das Team</span></div>
  <article class="abs house-card" style="left:218px">
    <div class="photo" role="img" aria-label="Gasthaus mit Fachwerkvorbau und Pflasterhof" style="background:linear-gradient(180deg,#b8c4cc 0%,#8c6b55 50%,#6f6a62 100%)"></div>
    <div class="kicker script-gold">Gaststätte</div>
    <h3>Genüßlich essen</h3>
    <p class="body-text">Wir haben bei uns im Lindenhof eine Wöchentlich Wechselnde Karte, mit Leckeren Fisch- und Fleischgerichte für Groß und Klein.</p>
  </article>
  <article class="abs house-card" style="left:489px">
    <div class="photo" role="img" aria-label="Pensionszimmer mit Doppelbett und violetten Vorhängen" style="background:linear-gradient(160deg,#8a6fa0 0%,#5a3f74 55%,#c8c2cc 100%)"></div>
    <div class="kicker script-gold">Pension</div>
    <h3>Hier finden Sie Ruhe</h3>
    <p class="body-text">Wir verfügen über 2 Pensionszimmer mit Doppelbetten in denen Sie einmal vollkommen abschalten können.</p>
  </article>
  <article class="abs house-card" style="left:760px">
    <div class="photo" role="img" aria-label="Eingang des Hofladens mit Schaufenster und Pflanzen" style="background:linear-gradient(180deg,#d9dde0 0%,#5a5550 55%,#8e8a86 100%)"></div>
    <div class="kicker script-gold">Hofladen</div>
    <h3>Wir beraten Sie gerne</h3>
    <p class="body-text">In unserem Ortsansässigen Hofladen, finden Sie alles was Sie als Fischliebhaber begehren.</p>
  </article>
</section>

<section class="daily">
  <div class="abs sec-kicker script-gold" style="top:1070px">Was gibt es zum Mittagessen?</div>
  <h2 class="abs sec-title script-head" style="top:1098px;font-weight:400">Sehen Sie sich unsere Tagesgerichte an</h2>
  <div class="abs dish" style="top:1172px"><span class="price">99,99€</span><h4>Lorem ipsum dolor sit amet</h4><p class="body-text">Lorem ipsum dolor sit amet, consetetur sadipscing elitr, sed diam nonumy eirmod tempor invidunt ut</p></div>
  <svg class="abs diamond" style="top:1258px" width="14" height="14" viewBox="0 0 14 14"><path d="M7 1 13 7 7 13 1 7Z" fill="none" stroke="#888"/><circle cx="7" cy="7" r="1.5" fill="#888"/></svg>
  <div class="abs dish" style="top:1288px"><span class="price">99,99€</span><h4>Lorem ipsum dolor sit amet</h4><p class="body-text">Lorem ipsum dolor sit amet, consetetur sadipscing elitr, sed diam nonumy eirmod tempor invidunt ut</p></div>
  <svg class="abs diamond" style="top:1374px" width="14" height="14" viewBox="0 0 14 14"><path d="M7 1 13 7 7 13 1 7Z" fill="none" stroke="#888"/><circle cx="7" cy="7" r="1.5" fill="#888"/></svg>
  <div class="abs dish" style="top:1404px"><span class="price">99,99€</span><h4>Lorem ipsum dolor sit amet</h4><p class="body-text">Lorem ipsum dolor sit amet, consetetur sadipscing elitr, sed diam nonumy eirmod tempor invidunt ut</p></div>
</section>

<section class="specials">
  <div class="abs sec-kicker script-gold" style="top:1620px">Spezialität</div>
  <h2 class="abs sec-title script-head" style="top:1650px;font-weight:400">Unsere Spezialitäten im Lindenhof</h2>
  <div class="abs chevrons center" style="left:0;width:1200px;top:1696px">» «</div>

  <article class="abs spec" style="left:220px;top:1782px">
    <div class="kicker script-gold">Neuste Speisen</div><h3>Lorem ipsum dolor</h3><div class="chevrons">» «</div>
    <p class="body-text">Lorem ipsum dolor sit amet, consetetur sadipscing elitr, sed diam nonumy eirmod tempor invidunt ut labore et dolore magna aliquyam</p>
    <span class="price">99,99€</span>
  </article>
  <div class="abs shot" role="img" aria-label="Frischer Fisch auf dunklem Brett mit Chili und Öl" style="left:624px;top:1769px;width:183px;height:264px;background:linear-gradient(170deg,#2a2826 0%,#5e6468 50%,#3a1e1a 100%)"></div>
  <div class="abs shot" role="img" aria-label="Fischfilet auf Schieferplatte" style="left:828px;top:1754px;width:182px;height:274px;background:linear-gradient(160deg,#1e1e1e 0%,#6b6866 55%,#2a2a2a 100%)"></div>

  <div class="abs shot" role="img" aria-label="Bier und gegrilltes Fleisch auf einem Tisch" style="left:218px;top:2119px;width:182px;height:272px;background:linear-gradient(180deg,#3a302a 0%,#b3823a 45%,#5c3a26 100%)"></div>
  <div class="abs shot" role="img" aria-label="Brot, eingelegte Peperoni und Rote Bete von oben" style="left:421px;top:2104px;width:182px;height:265px;background:linear-gradient(170deg,#2a2522 0%,#9a6a34 50%,#4a1e2a 100%)"></div>
  <article class="abs spec" style="left:639px;top:2116px">
    <div class="kicker script-gold">Neuste Speisen</div><h3>Lorem ipsum dolor</h3><div class="chevrons">» «</div>
    <p class="body-text">Lorem ipsum dolor sit amet, consetetur sadipscing elitr, sed diam nonumy eirmod tempor invidunt ut labore et dolore magna aliquyam</p>
    <span class="price">99,99€</span>
  </article>

  <article class="abs spec" style="left:220px;top:2488px">
    <div class="kicker script-gold">Neuste Speisen</div><h3>Lorem ipsum dolor</h3><div class="chevrons">» «</div>
    <p class="body-text">Lorem ipsum dolor sit amet, consetetur sadipscing elitr, sed diam nonumy eirmod tempor invidunt ut labore et dolore magna aliquyam</p>
    <span class="price">99,99€</span>
  </article>
  <div class="abs shot" role="img" aria-label="Gefüllte Gebäckröllchen mit Nüssen auf dunklem Grund" style="left:624px;top:2476px;width:183px;height:265px;background:linear-gradient(160deg,#2c2a28 0%,#7a5a44 50%,#2a2624 100%)"></div>
  <div class="abs shot" role="img" aria-label="Dessert mit Sirup und Beeren" style="left:828px;top:2461px;width:182px;height:272px;background:linear-gradient(180deg,#dfe2e4 0%,#d08a2a 55%,#8a2a2a 100%)"></div>
</section>

<section class="events">
  <div class="abs sec-kicker script-gold" style="top:2884px">Nicht Verpassen!</div>
  <h2 class="abs sec-title script-head" style="top:2914px;font-weight:400">Unsere Events</h2>
  <div class="abs chevrons center" style="left:0;width:1200px;top:2960px">» «</div>

  <article class="abs event" style="left:228px">
    <div class="photo" role="img" aria-label="Müsli mit Beeren und Nüssen" style="background:linear-gradient(160deg,#d8d2c8 0%,#3a3634 60%,#2a2826 100%)"></div>
    <h4>Lorem ipsum dolor sit</h4>
    <p>Lorem ipsum dolor sit amet, consetetur sadipscing elitr, sed diam nonumy eirmod tempor invidunt ut labore et dolore magna aliquyam</p>
    <div class="date">Feb 22, 2017</div>
  </article>
  <article class="abs event" style="left:427px">
    <div class="photo" role="img" aria-label="Spiegeleier in der Pfanne" style="background:linear-gradient(160deg,#2c2a28 0%,#c9c4bc 50%,#3a3634 100%)"></div>
    <h4>Lorem ipsum dolor sit</h4>
    <p>Lorem ipsum dolor sit amet, consetetur sadipscing elitr, sed diam nonumy eirmod tempor invidunt ut labore et dolore magna aliquyam</p>
    <div class="date">Feb 22, 2017</div>
  </article>
  <article class="abs event" style="left:625px">
    <div class="photo" role="img" aria-label="Pfannkuchen mit Früchten" style="background:linear-gradient(160deg,#3a3230 0%,#c88a4a 55%,#2c2826 100%)"></div>
    <h4>Lorem ipsum dolor sit</h4>
    <p>Lorem ipsum dolor sit amet, consetetur sadipscing elitr, sed diam nonumy eirmod tempor invidunt ut labore et dolore magna aliquyam</p>
    <div class="date">Feb 22, 2017</div>
  </article>
  <article class="abs event" style="left:822px">
    <div class="photo" role="img" aria-label="Gedeckter Tisch mit Speisen von oben" style="background:linear-gradient(160deg,#2a2624 0%,#b07a3a 50%,#5a2a2a 100%)"></div>
    <h4>Lorem ipsum dolor sit</h4>
    <p>Lorem ipsum dolor sit amet, consetetur sadipscing elitr, sed diam nonumy eirmod tempor invidunt ut labore et dolore magna aliquyam</p>
    <div class="date">Feb 22, 2017</div>
  </article>
  <div class="abs dots dark" style="left:593px;top:3382px"><span class="dot on"></span><span class="dot"></span><span class="dot"></span></div>
</section>

<section class="opening">
  <div class="abs hours" style="left:218px">
    <svg class="abs bump" width="60" height="15" viewBox="0 0 60 15"><path d="M0 15C14 15 16 1 30 1S46 15 60 15Z" fill="#161616"/></svg>
    <h3>Öffnungszeiten Hofladen</h3>
    <div class="orn"><svg width="12" height="12" viewBox="0 0 14 14"><path d="M7 1 13 7 7 13 1 7Z" fill="none" stroke="#666"/><circle cx="7" cy="7" r="1.5" fill="#666"/></svg></div>
    <div class="rule"></div>
    <ul>
      <li><span>Dienstag</span><span>14.00 – 18.00</span></li>
      <li><span>Donnerstag</span><span>14.00 – 18.00</span></li>
      <li><span>Freitag</span><span>14.00 – 18.00</span></li>
      <li><span>Samstag</span><span>09.00 – 14.00</span></li>
      <li><span>Sonntag</span><span>09.00 – 11.00</span></li>
    </ul>
  </div>
  <div class="abs hours" style="left:760px">
    <svg class="abs bump" width="60" height="15" viewBox="0 0 60 15"><path d="M0 15C14 15 16 1 30 1S46 15 60 15Z" fill="#161616"/></svg>
    <h3>Öffnungszeiten Gaststätte</h3>
    <div class="orn"><svg width="12" height="12" viewBox="0 0 14 14"><path d="M7 1 13 7 7 13 1 7Z" fill="none" stroke="#666"/><circle cx="7" cy="7" r="1.5" fill="#666"/></svg></div>
    <div class="rule"></div>
    <ul>
      <li><span>Freitag</span><span>17.00 – 24.00</span></li>
      <li><span>Samstag</span><span>11.00 – 24.00</span></li>
      <li><span>Sonntag</span><span>11.00 – 14.00</span></li>
      <li><span>Feiertags</span><span>11.00 – 14.00</span></li>
      <li><span>Mo. - Fr.</span><span>nach Absprache</span></li>
    </ul>
  </div>
</section>

<footer>
  <p class="abs address">Lindenhof Brauckmann | Lindenstraße 12 | 04720 Birkental | Tel.: 03431 / 558210 | mail@lindenhof-brauckmann.de</p>
  <svg class="abs" style="left:570px;top:3738px" width="60" height="15" viewBox="0 0 60 15"><path d="M0 15C14 15 16 1 30 1S46 15 60 15Z" fill="#161616"/></svg>
  <div class="abs footer"></div>
  <p class="abs footer-text" style="left:755px">Lindenhof Brauckmann 0.1 © 2021</p>
</footer>

</body>
</html>
```